Simple Clean Distinctive Fleet Graphic

Need design that can be used on truck (new Halden Brisk), and small/large cargo vans (new full size Halden cargoline, small size cargoline minor). Needs to include company logo, phone (555-310-4927) and “Service, Repair, Remodel” as the main focal point. Needs to also include “(Contractors License) or (CL) 58162,” which is a state requirement but not part of main focal point, just on bottom or off to the side in 2” letters/number.

Target Market(s)

Our core business is resort hotels, HOA's, and high end residential service and remodel projects.

Font styles to use
Sans Serif
Other font styles liked:
• logo is "what time is it" font

```html
<!DOCTYPE html>
<html lang="en">
<head>
<meta charset="utf-8">
<title>Tidewell Fleet Graphic</title>
<link href="https://fonts.googleapis.com/css2?family=Source+Sans+3:wght@400;600;700&display=swap" rel="stylesheet">
<style>
  :root {
    --bg: #ffffff;
    --brand-sky: #3ba6de;
    --brand-navy: #1f3f8f;
    --license-blue: #2d55b5;
    --ink: #1b1b1b;
  }
  * { margin: 0; padding: 0; box-sizing: border-box; }
  html, body {
    width: 1200px;
    height: 849px;
    overflow: hidden;
    background: var(--bg);
  }
  .fleet-graphic {
    width: 1200px;
    height: 849px;
    display: flex;
    flex-direction: column;
    align-items: center;
    justify-content: center;
    font-family: "Source Sans 3", "Helvetica Neue", Arial, sans-serif;
    color: var(--ink);
  }
  .brand-block {
    display: flex;
    flex-direction: column;
    align-items: flex-end;
  }
  .brand-lockup {
    display: flex;
    align-items: center;
    gap: 28px;
  }
  .brand-dot {
    width: 78px;
    height: 78px;
    border-radius: 50%;
    background: var(--brand-navy);
    flex: none;
  }
  .brand-name {
    font-size: 150px;
    font-weight: 600;
    line-height: 1;
    letter-spacing: -2px;
    color: var(--brand-sky);
  }
  .license-number {
    margin-top: 6px;
    margin-right: 8px;
    font-size: 26px;
    font-weight: 700;
    color: var(--license-blue);
    letter-spacing: 0.5px;
  }
  .service-line {
    margin-top: 34px;
    font-size: 82px;
    font-weight: 700;
    line-height: 1.05;
    letter-spacing: 0.5px;
  }
  .phone-number {
    margin-top: 18px;
    font-size: 86px;
    font-weight: 700;
    line-height: 1.05;
    letter-spacing: 1px;
  }
</style>
</head>
<body>
  <main class="fleet-graphic">
    <div class="brand-block">
      <div class="brand-lockup">
        <span class="brand-dot" aria-hidden="true"></span>
        <span class="brand-name">tidewell</span>
      </div>
      <p class="license-number">(CL) 58162</p>
    </div>
    <p class="service-line">Service, Repair, Remodel</p>
    <p class="phone-number">555-310-4927</p>
  </main>
</body>
</html>
```